Online-Marketing Material für Autohaus mit Werkstätten
Zielgruppe
Wir betreiben ein Autohaus mit Werkstätte und suchen hierfür Auszubildende in folgenden Berufen:
Kfz-Mechatroniker, Automobilkaufmann, Fachkraft für Lagerlogistik.
Aufgabenstellung
Die Post sollen Jugendliche ansprechen und sich an dem bisherigen Layout orientieren.

```html
<!DOCTYPE html>
<html lang="de">
<head>
<meta charset="utf-8">
<title>Ausbildung bei auto-wendel</title>
<link rel="stylesheet" href="https://fonts.googleapis.com/css2?family=Roboto:wght@400;700;900&display=swap">
<style>
  :root {
    --navy: #1d2b6b;
    --ink: #0d0d0d;
    --yellow: #f2ea1c;
    --white: #ffffff;
    --grey-light: #eef0f2;
    --grey-mid: #b9bec6;
    --grey-dark: #5c6470;
  }
  * { box-sizing: border-box; margin: 0; padding: 0; }
  html, body { width: 1200px; height: 1200px; overflow: hidden; background: var(--white); }
  .post {
    position: relative;
    width: 1200px;
    height: 1200px;
    overflow: hidden;
    font-family: "Roboto", Arial, sans-serif;
    color: var(--ink);
  }
  .showroom-photo {
    position: absolute;
    inset: 0;
    background:
      radial-gradient(ellipse 260px 520px at 1060px 760px, rgba(29,43,107,0.55), rgba(29,43,107,0) 75%),
      radial-gradient(ellipse 380px 300px at 560px 700px, rgba(70,76,88,0.35), rgba(70,76,88,0) 80%),
      linear-gradient(90deg, var(--white) 0%, var(--grey-light) 40%, var(--grey-mid) 72%, var(--grey-dark) 100%);
  }
  .text-fade {
    position: absolute;
    inset: 0;
    background: linear-gradient(90deg, rgba(255,255,255,0.92) 0%, rgba(255,255,255,0.7) 45%, rgba(255,255,255,0) 70%);
  }
  .brand {
    position: absolute;
    left: 112px;
    top: 112px;
    display: flex;
    align-items: center;
    gap: 12px;
    font-size: 36px;
    font-weight: 400;
    color: var(--navy);
  }
  .brand-mark { width: 18px; height: 18px; background: var(--navy); }
  .eyebrow {
    position: absolute;
    left: 114px;
    top: 336px;
    font-size: 25px;
    font-weight: 400;
    letter-spacing: 2px;
  }
  .headline {
    position: absolute;
    left: 110px;
    top: 408px;
    font-size: 81px;
    font-weight: 900;
    line-height: 82px;
    letter-spacing: 1px;
    text-transform: uppercase;
  }
  .headline-slash {
    display: inline-block;
    width: 34px;
    height: 48px;
    margin-left: 22px;
    vertical-align: -2px;
  }
  .jobs {
    position: absolute;
    left: 112px;
    top: 700px;
    font-size: 40px;
    font-weight: 400;
    line-height: 61px;
  }
  .apply-button {
    position: absolute;
    left: 112px;
    top: 913px;
    width: 538px;
    height: 84px;
    border-radius: 42px;
    background: var(--navy);
    color: var(--white);
    font-size: 27px;
    font-weight: 700;
    letter-spacing: 1px;
    display: flex;
    align-items: center;
    justify-content: center;
  }
  .contact {
    position: absolute;
    top: 1092px;
    display: flex;
    align-items: center;
    gap: 22px;
    font-size: 23px;
  }
  .contact-web { left: 112px; }
  .contact-mail { left: 588px; }
  .contact-icon { width: 52px; height: 52px; flex: none; }
  .chevrons { position: absolute; left: 1022px; top: 1100px; width: 74px; height: 38px; }
</style>
</head>
<body>
<main class="post">
  <div class="showroom-photo" role="img" aria-label="Foto: lächelnder junger Verkäufer im Anzug mit Tablet neben einem Auto im Autohaus"></div>
  <div class="text-fade"></div>

  <div class="brand"><span class="brand-mark"></span>auto-wendel</div>

  <p class="eyebrow">AUSBILDUNG</p>

  <h1 class="headline">
    Lust auf<br>
    eine Ausbildung<br>
    bei uns?<svg class="headline-slash" viewBox="0 0 34 48" aria-hidden="true"><polygon points="16,0 34,0 18,48 0,48" fill="var(--yellow)"/></svg>
  </h1>

  <p class="jobs">
    KFZ-Mechatroniker (m/w/d) /<br>
    Automobilkaufmann (m/w/d) /<br>
    Fachkraft für Lagerlogistik (m/w/d)
  </p>

  <div class="apply-button">JETZT BEWERBEN !</div>

  <div class="contact contact-web">
    <svg class="contact-icon" viewBox="0 0 52 52" aria-hidden="true">
      <circle cx="26" cy="26" r="26" fill="var(--navy)"/>
      <g fill="none" stroke="var(--white)" stroke-width="2">
        <circle cx="26" cy="26" r="13"/>
        <ellipse cx="26" cy="26" rx="6" ry="13"/>
        <line x1="13" y1="26" x2="39" y2="26"/>
        <line x1="15" y1="19" x2="37" y2="19"/>
        <line x1="15" y1="33" x2="37" y2="33"/>
      </g>
    </svg>
    <span>www.kfzjobs.autowendel.de</span>
  </div>

  <div class="contact contact-mail">
    <svg class="contact-icon" viewBox="0 0 52 52" aria-hidden="true">
      <circle cx="26" cy="26" r="26" fill="var(--navy)"/>
      <circle cx="26" cy="26" r="15" fill="none" stroke="var(--white)" stroke-width="2"/>
      <rect x="17" y="20" width="18" height="12" rx="1.5" fill="var(--white)"/>
      <polyline points="17,20 26,27 35,20" fill="none" stroke="var(--navy)" stroke-width="1.8"/>
    </svg>
    <span>jwendel@autowendel.de</span>
  </div>

  <svg class="chevrons" viewBox="0 0 74 38" aria-hidden="true">
    <g fill="none" stroke="var(--yellow)" stroke-width="3.5">
      <polyline points="3,3 18,19 3,35"/>
      <polyline points="28,3 43,19 28,35"/>
      <polyline points="53,3 68,19 53,35"/>
    </g>
  </svg>
</main>
</body>
</html>
```